Business Cards Design for the electrical wholesaler: clean bold dynamic :)

We need a business card design that would follow our latest brand guidelines. As an electrical wholesaler we want to bring a fresh look and feel into the industry. The design should be clean bold and dynamic. It should come alive with the renewed energy of our green colour. Our grey colour should keep things balanced and complement the notion of maturity and responsibility. We employ Lato as a corporate font however are not bound by this font and we’re open to interpretation here.

Target Market(s)

Electrical contractors

Industry/Entity Type

Business

Contact Information for Business Card

Logo
Name & Surname: Olena Dovbush
Job Title: Director of Marketing
Email: helen.dovbush@mailvane.example
Cell phone: XXX.XXX.XXXX
Address: 20917 - 87 Ave. Edmonton, AB, Canada. T6K 2R8
Business Phone: 780.555.0187
Website: www.qorvil.example

Font styles to use
Other font styles liked:
• Lato

Requirements
Must have
• Logo & website
Nice to have
• Brand elements - some of them you may find in the attached Brand Guidelines (e.g. three lines on the background signifying "W")

```html
<!DOCTYPE html>
<html lang="en">
<head>
<meta charset="utf-8">
<title>Qorvil business cards</title>
<link rel="stylesheet" href="https://fonts.googleapis.com/css2?family=Lato:wght@400;700;900&display=swap">
<style>
  :root {
    --green: #6cbf43;
    --green-light: #84c653;
    --green-deep: #5aab35;
    --grey: #434647;
    --text: #3d4042;
    --text-soft: #666a6c;
    --paper: #ffffff;
    --backdrop: #e9ebec;
  }
  * { box-sizing: border-box; margin: 0; padding: 0; }
  html, body { width: 1200px; height: 934px; overflow: hidden; }
  body {
    background: var(--backdrop);
    font-family: "Lato", Arial, sans-serif;
    color: var(--text);
    display: flex;
    align-items: center;
    justify-content: center;
    gap: 60px;
  }
  .card {
    position: relative;
    width: 520px;
    height: 300px;
    overflow: hidden;
    box-shadow: 0 10px 24px rgba(0,0,0,0.12);
  }
  /* front */
  .card-front { background: var(--green); }
  .front-field {
    position: absolute;
    inset: 0;
    background: radial-gradient(ellipse at 70% 35%, var(--green-light) 0%, var(--green) 55%, var(--green-deep) 100%);
  }
  .front-brand {
    position: absolute;
    left: 60px;
    bottom: 70px;
    display: flex;
    align-items: center;
    gap: 14px;
  }
  .brand-dot {
    width: 30px;
    height: 30px;
    border-radius: 50%;
    background: var(--grey);
  }
  .brand-name {
    font-weight: 900;
    font-size: 54px;
    line-height: 1;
    color: var(--grey);
    letter-spacing: -0.5px;
  }
  /* back */
  .card-back { background: var(--paper); }
  .band-grey {
    position: absolute;
    left: 0; top: 96px;
    width: 196px; height: 22px;
    background: var(--grey);
  }
  .band-green {
    position: absolute;
    right: 0; top: 0;
    width: 220px; height: 20px;
    background: var(--green);
  }
  .back-brand {
    position: absolute;
    left: 206px;
    top: 70px;
    display: flex;
    align-items: center;
    gap: 10px;
  }
  .back-brand .brand-dot { width: 22px; height: 22px; }
  .back-brand .brand-name { font-size: 46px; }
  .person {
    position: absolute;
    left: 36px;
    top: 186px;
    width: 228px;
    font-size: 13px;
    line-height: 1.4;
  }
  .person-name {
    font-weight: 900;
    font-size: 19px;
    color: var(--green);
    line-height: 1.1;
  }
  .person-role { color: var(--text-soft); font-size: 13px; margin-bottom: 2px; }
  .divider {
    position: absolute;
    left: 274px; top: 158px;
    width: 1px; height: 120px;
    background: var(--grey);
  }
  .contacts {
    position: absolute;
    left: 288px;
    top: 162px;
    width: 220px;
    list-style: none;
    font-size: 12px;
    line-height: 1;
  }
  .contacts li {
    display: flex;
    align-items: center;
    gap: 8px;
    height: 25px;
    white-space: nowrap;
  }
  .contacts svg { width: 14px; height: 14px; flex: none; }
</style>
</head>
<body>
  <section class="card card-front" aria-label="Card front">
    <div class="front-field" role="img" aria-label="Green field with faint brand stripe decoration"></div>
    <div class="front-brand">
      <span class="brand-dot"></span>
      <span class="brand-name">Qorvil</span>
    </div>
  </section>

  <section class="card card-back" aria-label="Card back">
    <div class="band-grey"></div>
    <div class="band-green"></div>
    <div class="back-brand">
      <span class="brand-dot"></span>
      <span class="brand-name">Qorvil</span>
    </div>

    <div class="person">
      <p class="person-name">Olena Dovbush</p>
      <p class="person-role">Director of Marketing</p>
      <p>20917 - 87 Ave. Edmonton</p>
      <p>AB Canada. T6K 2R8</p>
    </div>

    <div class="divider"></div>

    <ul class="contacts">
      <li>
        <svg viewBox="0 0 16 16" aria-hidden="true"><circle cx="8" cy="8" r="7" fill="none" stroke="var(--green)" stroke-width="1.6"/><path d="M5 5.5c0 3 2.5 5.5 5.5 5.5l.8-1.4-1.6-.9-.8.8c-1-.4-1.9-1.3-2.3-2.3l.8-.8-.9-1.6z" fill="var(--green)"/></svg>
        780.555.0187
      </li>
      <li>
        <svg viewBox="0 0 16 16" aria-hidden="true"><rect x="4" y="1" width="8" height="14" rx="1.5" fill="none" stroke="var(--green)" stroke-width="1.5"/><circle cx="8" cy="12.3" r="0.9" fill="var(--green)"/></svg>
        780.555.0142
      </li>
      <li>
        <svg viewBox="0 0 16 16" aria-hidden="true"><rect x="1" y="3.5" width="14" height="9" fill="var(--green)"/><path d="M1 3.5l7 5 7-5" fill="none" stroke="#fff" stroke-width="1.2"/></svg>
        helen.dovbush@mailvane.example
      </li>
      <li>
        <svg viewBox="0 0 16 16" aria-hidden="true"><circle cx="8" cy="8" r="7" fill="none" stroke="var(--green)" stroke-width="1.5"/><path d="M1 8h14M8 1c-3 3.5-3 10.5 0 14M8 1c3 3.5 3 10.5 0 14" fill="none" stroke="var(--green)" stroke-width="1.1"/></svg>
        www.qorvil.example
      </li>
    </ul>
  </section>
</body>
</html>
```